Sir Trimwell Beard Oil labels for 2oz bottle and a label for its box

I am looking to design a label for a 2oz beard oil glass bottle as well as its box. This is for a new company so the design should be high fidelity and captivating. Ideally I would like a picture on the bottle of a mans face at a 45 degree angle. His beard will be curly/course and full. Something like the uploaded file in a fuller more detailed way (Without the beanie), he can be bald. The characters mouth does not necessarily have to be opened and should not be Corwin Tase since I don't have rights to use his photo on a product. I'm looking to use earthy tones for the bottle label and box that bleeds sophistication with a modern urban hint to it. The product will boast a perfect blend of 6 key oils that work best for hair follicles that struggle to retain moisture. Leaving it soft and moisturized without an unpleasant smell.

Back label of box should read:

Beard care has been passed down for generations and is only now becoming a popular trend. Sir Trimwell’s beard products formulated for tightly coiled and kinky hair, has mastered the science over the years, to bring you a specifically refined product that is guaranteed to let the mane reign!

With a proper washing routine, Sir Trimwell beard oil is guaranteed to leave your beard moisturized, itch and dandruff free without any chemicals. Sir Trimwells oil mixture is 100% natural and organic, so you know you're getting the best. Sir Trimwell’s beard oil is uniquely different for a unique difference.

"The essence of a mans style is what he puts on, so it better Trimwell"

Target Market(s)

African Americans and Individuals with hair follicles that do not retain much moisture.

Industry/Entity Type

Hair And Beauty

Font styles to use
Decorative
Script

Colors
000000
757575
f37122
faa54b
f78f20
ec1f27
9bcb3b
ffffff

Requirements
Must have
• A captivating character (Vector File) on the front of the bottle that has a kinky, curly beard. I would like the character to resemble the cartoonish style features of the plainfield farmer character I included in the attached picture, however make him look more black (African American)
• Also the box rear label needs to have the descriptive last 2 paragraphs I included in the project description. The last sentence "The essence of a mans style is what he puts on, so it better Trimwell" should be at the very bottom of the box front or back, whichever looks best.
• Main colors are tan (Label base), black (lettering), Red (Slight accenting), the rest is up to you. I want the label to have primarily earth tones, brown, tan, green.
Nice to have
• Sir Trimwell Beard Oil lettering would preferably be in black, with a thin outlining of Red. As for the bottle I would prefer it be a tan label with black and grey lettering with very slight accenting of any color you think would look best with my design. The colors I chose below are just guidelines, except for the shades of tan. I would like the box to incorporate a shade of tan with the other colors making up the designs and letters
Should not have
• Label lettering on back of box should not be in script. Script should not be too distracting. The red should not overpower the labels at all. Almost none existent yet noticeable. The brighter colors should not make up more than 20% of the label

```html
<!DOCTYPE html>
<html lang="en">
<head>
<meta charset="utf-8">
<title>Sir Trimwell Beard Oil – Box and Bottle Label</title>
<link href="https://fonts.googleapis.com/css2?family=PT+Serif:ital,wght@0,400;0,700;1,400&family=Griffy&display=swap" rel="stylesheet">
<style>
:root{
  --backdrop:#ecebe7;
  --tan:#ead7b3;
  --tan-light:#f1e3c6;
  --tan-line:#f6ecd9;
  --maroon:#7e2b2d;
  --ink:#1f1b18;
  --body:#3f352e;
  --art:#a8574f;
}
*{margin:0;padding:0;box-sizing:border-box}
html,body{width:1200px;height:959px;overflow:hidden;background:var(--backdrop)}
body{position:relative;font-family:"PT Serif",serif;color:var(--body)}
.panel{position:absolute;background:var(--tan);box-shadow:0 2px 10px rgba(0,0,0,.12)}

/* box back / side panel */
.box-side{left:40px;top:40px;width:250px;height:870px;padding:40px 22px 0;text-align:center}
.story p{font-size:13px;line-height:1.55;margin-bottom:16px}
.side-mark{margin:14px auto 0;display:flex;flex-direction:column;align-items:center}
.side-mark .portrait{width:40px;height:58px;border-radius:50%;background:var(--art)}
.side-mark .brand{font-weight:700;font-size:16px;color:var(--ink);margin-top:6px}
.maker{text-align:left;margin-top:22px;font-size:12px;line-height:1.5}
.maker h4{font-weight:400;font-size:15px;margin-bottom:10px}
.flag{width:42px;height:26px;background:#b4434a;margin-top:14px;border-radius:2px}
.side-band{position:absolute;left:0;right:0;bottom:0;height:104px;background:var(--maroon);color:#fff;
  font-style:italic;font-size:14px;line-height:1.35;display:flex;align-items:center;justify-content:center;padding:0 20px;text-align:center}

/* box front */
.box-front{left:300px;top:40px;width:380px;height:870px;display:flex;flex-direction:column;align-items:center}
.top-band{width:100%;height:50px;background:var(--maroon);flex:none}
.flourish{width:170px;height:56px;margin-top:40px;background:var(--tan-line);border-radius:30px;flex:none}
.front-portrait{width:220px;height:190px;margin-top:100px;border-radius:50%;background:var(--art);flex:none}
.brand-name{font-weight:700;color:var(--ink);letter-spacing:-1px;line-height:1}
.box-front .brand-name{font-size:52px;margin-top:30px}
.product{display:flex;align-items:center;margin-top:30px}
.product .rule{width:34px;height:1px;background:var(--maroon)}
.product .pill{background:var(--maroon);color:var(--tan-light);font-family:"Griffy",cursive;font-size:26px;
  padding:2px 14px;border-radius:6px;line-height:1.3}
.size{font-size:22px;color:var(--ink);letter-spacing:.5px;line-height:1.2}
.box-front .size{margin-top:120px}
.front-quote{width:100%;border-top:6px solid var(--tan-line);border-bottom:6px solid var(--tan-line);
  padding:12px 30px;text-align:center;color:var(--maroon);font-size:17px;line-height:1.3;margin-top:22px}

/* bottle label */
.bottle-label{left:720px;top:190px;width:440px;height:560px;background:var(--tan-light);
  display:flex;flex-direction:column;align-items:center}
.label-portrait{width:190px;height:170px;margin-top:60px;border-radius:50%;background:var(--art)}
.bottle-label .brand-name{font-size:54px;margin-top:42px}
.bottle-label .product{margin-top:38px}
.bottle-label .size{margin-top:26px}
</style>
</head>
<body>

<section class="panel box-side" aria-label="Box back panel">
  <div class="story">
    <p>Beard care has been passed down for generations and is only now becoming a popular trend. Sir Trimwell’s beard products formulated for tightly coiled and kinky hair, has mastered the science over the years, to bring you a specifically refined product that is guaranteed to let the mane reign!</p>
    <p>With a proper washing routine, Sir Trimwell beard oil is guaranteed to leave your beard moisturized, itch and dandruff free without any chemicals.</p>
    <p>Sir Trimwells oil mixture is 100% natural and organic, so you know you're getting the best. Sir Trimwell’s beard oil is uniquely different for a unique difference.</p>
  </div>
  <div class="side-mark">
    <div class="portrait" role="img" aria-label="Small illustration of the bearded mascot"></div>
    <div class="brand">Sir Trimwell</div>
  </div>
  <div class="maker">
    <h4>Manufactured By:</h4>
    <div>Company Name<br>And the address may be<br>here. 00000 Country<br>visit us:<br>www.sirtrimwell-oils.com</div>
    <div class="flag" role="img" aria-label="Country of origin flag"></div>
  </div>
  <div class="side-band">“The essence of a mans style is what he puts on, so it better Trimwell”</div>
</section>

<section class="panel box-front" aria-label="Box front panel">
  <div class="top-band"></div>
  <div class="flourish" role="img" aria-label="Decorative flourish ornament"></div>
  <div class="front-portrait" role="img" aria-label="Illustration of the bearded mascot in a red oval"></div>
  <div class="brand-name">Sir Trimwell</div>
  <div class="product"><span class="rule"></span><span class="pill">Beard Oil</span><span class="rule"></span></div>
  <div class="size">2 oz (60 ml)</div>
  <div class="front-quote">“The essence of a mans style is what he puts on, so it better Trimwell”</div>
</section>

<section class="panel bottle-label" aria-label="Bottle label">
  <div class="label-portrait" role="img" aria-label="Illustration of the bearded mascot in a red oval"></div>
  <div class="brand-name">Sir Trimwell</div>
  <div class="product"><span class="rule"></span><span class="pill">Beard Oil</span><span class="rule"></span></div>
  <div class="size">2 oz (60 ml)</div>
</section>

</body>
</html>
```